Online travel site needs edgy website design

tripvane is the first Global Business Travel Website that provides the most comprehensive destination information tailored to suit the business traveller.

It is a ‘one click solution’ that offers direct access to all aspects of business travel, including general information on the city, accommodation and transportation options, economic and financial statistics, key business and services contacts, as well as leisure activities, entertainment suggestions, and listings for any personal needs.

Much more than a travel website, tripvane.com eliminates the need to buy multiple travel books or visit scores of websites. Most importantly, it is the only website that will cover such an extensive range of destinations around the world, while also featuring cities where information is really scarce. The user-friendly and consistent format for all destinations will allow the business traveller to easily navigate through more than 100 information pages on any destination.

tripvane will be simple to navigate, intuitive, unique in design, dynamic, and content rich providing a supreme user experience during navigation of the website.

The website will initially be English and is set to expand to more languages in the future.

A beta site with back-end database has been built - and now we need an edgy state of the art graphic design to reskin it.

LOOK & FEEL

Scope
The design of the site should reflect tripvane’s corporate and user centric philosophy with the following elements:

a. tripvane corporate image and branding
b. the promotion of each city destination
c. tripvane being the starting point of travel, while also a partner during travel
d. the subtle but powerful presence of advertising and sponsorship

All the above must derive from the design outline and elements that are going to be used.

Design Guidelines

Innovative and elegant design, minimalism, simplicity that permits the offering of the required information to be delivered in line with the values of Trust, Care, Discovery & Connection.

In addition:

1. The usability, navigation and the informative character of the corporate web site should not be compromised by the design.
2. The over-segmented pages and over-crowded content per page should be avoided.
3. The design should not only guide the user in an inviting way to the information required but also to intrigue them for further navigation.
4. Advertising space should be anticipated in line with the design character and DMQ standard ad sizes.
5. The use of photos / videos should also encouraged.

Key Elements

a. Branding/Logos
Throughout the website branding should be present as a “guarantee seal” for the content accuracy. Corporate logo should be placed on every page while branding should also characterise any content element and/or tool. Appendix contains the current brand guidelines. Should additional sub-logos be required for specific sections, these should be proposed.

b. Fonts
Provided your experience on the website design you are requested to propose alternative font types and sizes always taken into consideration the inviting and user friendly character that the new website should aspire to. The font type that will be proposed must be user friendly in English typography, but also could support other languages in the future.

Given the fact that the majority of the text in the website contains information and listing, the fonts and text layout should not strain and fatigue the reader.

c. SEO
The design should be friendly towards the search engines.

d. Colours
Colour is considered as an integral part of the brand identity. Tripvane.com corporate colours are orange and grey as per the Attached document reference guide.

Different tonalities of the brand colours, or colours in general, should be proposed and applied, guided always by the above described scope of Look & Feel.

e. Section Headings
As presented above, the site’s section headings (refer Overview of the Site.) The principle is to label the content following users’ needs and mindset. However, the label space should be flexible for changes. The labels should facilitate the user to understand the content they host. This is important and should be applied especially to informative content.

Another function that Headings should perform is that of promoting the website’s content, especially when this kind of content will make the user spend more time in the website. This category of Headings should be approached in a more creative and attractive way as to intrigue users to check the content hosted.

f. Icons
Icons are considered necessary in order to provide the user extra help to guide them to reach the information they need quick n’ easy. Icons not only contribute actively to the creation of an attractive look & feel but, most importantly, facilitate navigation and speed up the users’ familiarisation with the website too.

Therefore their design should be eye-catching, comprehensive and dynamic, in accordance to the new site’s colour coding and following the latest trends as these were defined by the look & feel of smart phones.

PIXELHIVE BRIEF REQUIREMENTS
Based on the above, please provide at least two (2) approaches for the following pages – this includes colour palette in line with logo, layout, fonts.

Initial submissions can just address Deliverable 1 & 2 to fine tune design before proceeding further.

Please refer sample screenshots separately attached from raw beta site for content – available for Deliverables 2 -6.

(REFER example sites we like for their creativity: http://www.brindle-studio.example.co.uk/#Background, http://www.rotaclarafestas.example.com.br/, http://pembrookweb.example.co.uk/ )

Deliverable 1: Landing /Home page
- Access log in –
o Free Account or via Workloop/Chatterbox etc
o Membership Access – Login
- How to use the site
- Allowance for video or animation
- Destination Selection
- Blog & Social media links

Deliverable 2: Destination Landing Page / Template
This is essentially a city guide template to be used for all cities throughout the site.

This page clearly depicts the four information sections
1. General
2. Business
3. Leisure
4. Personal

Also this page should include:
- Business News Feed
- Advertising & Sponsorship Spaces (according to DMQ Standards)
- Destination Time, Weather, FX rates (LIVE feeds)
- Tips

Deliverable 3: Follow the above format but show an Internal Content Page – text only with subheadings

Deliverable 4: Follow the above format but show an Internal Content Page – text and photos

Deliverable 5: Follow the above format but show an Internal Content Page – Listing Sections such as Restaurants (this must also include filter categories)

Deliverable 6: Follow the above format but show an Internal Content Page – Top 10 Experiences – this incorporates address and contact details, photo and sub-text

Deliverable 7: The Membership Landing Page which should include:
1. Intro
2. Advertising & Sponsorship Space
3. The four sections
4. Tips Section
Updates

Hi all - just to reiterate that we are open to different approaches in the design.  We only included the existing screen shots of the beta site to provide you with an idea of the content.  We definitely don't want to see anything similar.....we want it to be edgy yet simple and easy to navigate....we want to create an outstanding user experience!  Cheers Tripvane Team

Reason: Dear Designers - We are extending the period as have not had many submissions at all and want to provide more time. If you have already submitted, we will be in touch shortly with feedback. Thanks for your understanding Tripvane Team

Reason: We would like to give everyone more time so we can find the best and most preferred design.

Target Market(s)

TARGET MARKET
tripvane is a consumer focused website, offering a wide-range of easy-to-use and interactive platforms, for informative and commercial purposes, while also providing attractive and innovative advertising real-estate for potential business partners.

The target audience can be segmented as follows:

Primary Target: Professionals travelling on Business

They require up-to-date reliable information prior and during their travel, as well as facilitation to take action. They need an online Personal Assistant.

The personal characteristics of the primary target group are: busy life, tailored solutions, reliable sources, trusting, caring, and spoiled.
 
The website will have a membership option (for a small annual fee) which will provide customized information for their demographic and preferences. Sub target groups will include:
1. Business Men 40 years
3. Business Women 40 years
5. Business People with reduced mobility

Demographic & Travelling Profile of Business Travellers

• 92% of them use the internet as a source of info
• 54% are males, 38 years old
• 80% holds a college/university degree
• 68% is travelling mainly for leisure and annually 6 times per year
• 52% reserve their ticket through the internet
• 66% is travel internationally

Secondary Targets:

Executive PA’s
Executive personal assistants who need to plan their manager’s travel and provide support information for their trip.

Professionals travelling for Leisure and Partners
They have most probably used the website for their business travel, but consider it also useful for their leisure travel. The generic website, will include enough information to cover most of the leisure needs, as well as the requirements of their partners.

Direct Business-to-Business [B2B] Targets
The direct [B2B] targeted audience includes corporations that would like to use a white label solution for their staff, by using all available destinations or a selected number depending on their global network.

Business-to-Business [B2B] Targets
The [B2B] targeted audience is an indirect audience, for which tripvane promotes its services, and a key revenue stream. The B2B audience consists mainly of a diverse range of professional organisations targeting the business traveller (airlines, hotels, travel agencies, tourism authorities, entertainment companies, services, etc.) tripvane will be targeting these organisations to advertise on the site.
 
Desired Response from Target Groups

The desired response from the consumer targets is:
a) Recurrent use of website
b) Share content/experience with friends and social networking sites
c) Interact on the website’s Blog
d) Register for newsletters and offers
e) Subscribe to Membership
f) Be exposed to commercial advertisements on the website
g) Provide feedback (in the future) for services
h) Use (in the future) online services to purchase products and services
Competition

Industry/Entity Type

Travel

Requirements
Must have
• A clean crisp and professional appearance giving a sense of Trust and Reliability.
Should not have
• It should not look like every other run of the mill travel sites - Roomly.com, Wanderpost etc

```html
<!DOCTYPE html>
<html lang="en">
<head>
<meta charset="utf-8">
<title>tripvane — Global Business Travel</title>
<link href="https://fonts.googleapis.com/css2?family=Courgette&family=Lato:wght@400;700&family=Open+Sans:wght@600;700&display=swap" rel="stylesheet">
<style>
:root{
  --orange:#f7870f;
  --orange-light:#fb9a25;
  --orange-text:#f28a1a;
  --grey-dark:#4c4c4c;
  --grey-text:#555;
  --grey-mid:#7a7a7a;
  --page:#f2f2f2;
  --panel:#eeeeee;
  --panel-border:#e0e0e0;
  --blue-deep:#1b9be3;
  --blue-button:#1e6ff0;
  --footer:#1c9fe6;
  --white:#ffffff;
}
*{box-sizing:border-box;margin:0;padding:0}
html,body{width:931px;height:1200px;overflow:hidden}
body{background:var(--page);font-family:'Lato',sans-serif;color:var(--grey-text);position:relative}
.top-rule{position:absolute;left:0;top:0;width:931px;height:4px;background:var(--orange-light)}

/* header */
.account-tab{position:absolute;left:754px;top:0;width:124px;height:37px;background:var(--orange);border-radius:0 0 10px 10px;color:var(--white);font-family:'Courgette',cursive;font-size:13px;display:flex;align-items:center;justify-content:center;gap:8px}
.phone{position:absolute;left:762px;top:50px;display:flex;align-items:center;gap:8px;color:var(--orange-text);font-family:'Open Sans',sans-serif;font-weight:700;font-size:14px}
.phone-dot{width:17px;height:17px;border-radius:50%;background:var(--blue-deep)}
.brand{position:absolute;left:38px;top:42px;display:flex;align-items:center;gap:12px}
.brand-square{width:56px;height:56px;background:var(--orange);border-radius:4px}
.brand-name{font-family:'Open Sans',sans-serif;font-weight:600;font-size:46px;color:var(--grey-dark);letter-spacing:-1px;line-height:1}
.main-nav{position:absolute;left:41px;top:154px;width:840px;display:flex;justify-content:space-between;font-family:'Courgette',cursive;font-size:15px;color:var(--grey-dark)}
.main-nav .active{color:var(--orange)}
.nav-rule{position:absolute;left:0;top:196px;width:931px;height:1px;background:#e2e2e2}

/* hero */
.hero{position:absolute;left:0;top:197px;width:931px;height:333px;background:linear-gradient(180deg,#2aa9ee 0%,#3db6f2 70%,#5cc4f4 100%);overflow:hidden}
.hero-art{position:absolute;left:400px;top:20px;width:500px;height:260px;border-radius:50%;background:radial-gradient(ellipse at 50% 45%,rgba(255,255,255,.5) 0%,rgba(150,215,250,.3) 40%,rgba(60,180,240,0) 70%)}
.hero-fade{position:absolute;left:0;bottom:0;width:931px;height:95px;background:linear-gradient(180deg,rgba(255,255,255,0) 0%,rgba(255,255,255,.75) 55%,#ffffff 100%)}
.hero-title{position:absolute;left:32px;top:34px;font-family:'Courgette',cursive;font-weight:400;font-size:29px;color:var(--white)}
.hero-copy{position:absolute;left:32px;top:88px;width:350px;font-size:13.5px;line-height:19px;color:var(--white)}
.btn{position:absolute;display:flex;align-items:center;justify-content:center;font-family:'Courgette',cursive;color:var(--white);border-radius:7px}
.btn-member{left:32px;top:205px;width:163px;height:46px;background:var(--orange);font-size:20px}
.btn-social{left:205px;top:205px;width:181px;height:46px;background:var(--blue-button);font-size:20px}

/* how to use */
.panel{position:absolute;background:var(--panel);border:1px solid var(--panel-border);border-radius:4px}
.howto{left:32px;top:564px;width:855px;height:352px}
.section-title{font-family:'Courgette',cursive;font-weight:400;color:var(--grey-dark)}
.howto .section-title{position:absolute;left:19px;top:26px;font-size:28px}
.howto-copy{position:absolute;left:19px;top:76px;width:296px;font-size:13px;line-height:19px;color:var(--grey-mid)}
.howto-copy p+p{margin-top:19px}
.btn-read{left:16px;top:243px;width:125px;height:45px;background:var(--orange);font-size:19px}
.video{position:absolute;left:328px;top:17px;width:512px;height:312px;background:#111;padding:6px 6px 0 6px}
.video-still{width:500px;height:280px;background:linear-gradient(135deg,#f4f4f4 0%,#d9dde2 45%,#9aa7b5 75%,#e8ecef 100%)}
.video-play{position:absolute;left:235px;top:112px}
.video-bar{position:absolute;left:0;bottom:0;width:512px;height:24px;background:#1b1b1b;display:flex;align-items:center;gap:12px;padding-left:14px;color:#ccc;font-size:10px}
.video-progress{position:absolute;left:0;top:-3px;width:512px;height:3px;background:#444}
.video-progress span{display:block;width:135px;height:3px;background:#d22}

/* cards */
.card{top:932px;width:276px;height:160px}
.card .section-title{position:absolute;left:13px;top:10px;font-size:23px}
.card-dest{left:32px}
.card-blog{left:322px}
.card-touch{left:611px}
.select{position:absolute;left:13px;top:58px;width:232px;height:32px;background:var(--white);border:1px solid #cfcfcf;font-size:10px;color:#888;display:flex;align-items:center;justify-content:space-between;padding:0 10px}
.btn-small{height:31px;background:var(--orange);font-size:17px}
.card-dest .btn-small{left:13px;top:104px;width:108px}
.card-blog p{position:absolute;left:13px;top:50px;width:250px;font-size:12px;line-height:15px;color:var(--grey-text)}
.card-blog .btn-small{left:13px;top:104px;width:131px}
.card-touch p{position:absolute;left:30px;top:50px;width:232px;font-size:12px;line-height:15px;color:var(--grey-text)}
.social{position:absolute;left:32px;top:92px;display:flex;gap:10px}
.social span{width:22px;height:24px;border-radius:3px}
.s1{background:#3b5a98}.s2{background:#33b5e8}.s3{background:#333}.s4{background:#0e76a8}.s5{background:#e6e6e6}

/* footer */
.site-footer{position:absolute;left:0;top:1111px;width:931px;height:89px;background:var(--footer);color:var(--white);font-family:'Courgette',cursive}
.footer-nav{position:absolute;left:0;top:22px;width:931px;display:flex;justify-content:center;gap:24px;font-size:10px}
.copyright{position:absolute;left:0;top:60px;width:931px;text-align:center;font-size:11px}
</style>
</head>
<body>
<div class="top-rule"></div>

<header>
  <div class="account-tab"><span>Login</span><span>|</span><span>Sign Up</span></div>
  <div class="phone"><span class="phone-dot"></span>555 014 2290</div>
  <div class="brand"><span class="brand-square"></span><span class="brand-name">tripvane</span></div>
  <nav class="main-nav">
    <span class="active">Home</span><span>About Us</span><span>How to Use</span><span>Select Destination</span><span>Register</span><span>My Account</span><span>Blog</span><span>Contact Us</span>
  </nav>
  <div class="nav-rule"></div>
</header>

<section class="hero">
  <div class="hero-art" role="img" aria-label="Glowing world map with abstract light swirls"></div>
  <div class="hero-fade" role="img" aria-label="Soft band of white clouds along the lower edge"></div>
  <h1 class="hero-title">Lorem Ipsum dolor sit amet</h1>
  <p class="hero-copy">Lorem ipsum dolor sit amet, consectetur adipiscing elit. Donec facilisis turpis augue, sit amet lacinia neque tempor sed. Consectetur adipiscing elit. Donec facilisis turpis augue</p>
  <a class="btn btn-member">Member Login</a>
  <a class="btn btn-social">Chatterbox Login</a>
</section>

<section class="panel howto">
  <h2 class="section-title">How to use the site</h2>
  <div class="howto-copy">
    <p>Donec malesuada vehicula ipsum, eget dictum mauris laoreet et. Nam id est ante. Curabitur eget nibh et mi ultrices vestibulum.</p>
    <p>Morbi volutpat, felis quis iaculis vulputate, tellus sapien mattis sem, eget malesuada diam metus ut tortor. Aliquam sed cursus leo. Mauris eu eros et nibh dictum dictum nec a augue.</p>
  </div>
  <a class="btn btn-read">Read More</a>
  <div class="video">
    <div class="video-still" role="img" aria-label="Video still of a business team gathered around a globe"></div>
    <svg class="video-play" width="42" height="42" viewBox="0 0 42 42" aria-hidden="true">
      <circle cx="21" cy="21" r="19" fill="#2aa8ee" stroke="#fff" stroke-width="3"/>
      <path d="M16 12 L31 21 L16 30 Z" fill="#fff"/>
    </svg>
    <div class="video-bar">
      <div class="video-progress"><span></span></div>
      <span>❚❚</span><span>◀)</span><span>0:14 / 4:05</span>
    </div>
  </div>
</section>

<section class="panel card card-dest">
  <h2 class="section-title">Select Destination</h2>
  <div class="select"><span>Select City</span>
    <svg width="12" height="8" viewBox="0 0 12 8" aria-hidden="true"><path d="M1 1 L6 6 L11 1" fill="none" stroke="#222" stroke-width="2"/></svg>
  </div>
  <a class="btn btn-small">Submit</a>
</section>

<section class="panel card card-blog">
  <h2 class="section-title">Latest Blog</h2>
  <p>Morbi volutpat, felis quis iaculis vulputate, tellus sapien mattis sem, eget malesuada diam metus.</p>
  <a class="btn btn-small">More Post</a>
</section>

<section class="panel card card-touch">
  <h2 class="section-title">Get In Touch</h2>
  <p>Pleae clcik on the icons and get in ytouch with us and get all the updates.</p>
  <div class="social"><span class="s1"></span><span class="s2"></span><span class="s3"></span><span class="s4"></span><span class="s5"></span></div>
</section>

<footer class="site-footer">
  <nav class="footer-nav">
    <span>Home</span><span>|</span><span>About Us</span><span>|</span><span>FAQs</span><span>|</span><span>SiteMap</span><span>|</span><span>Contact Us</span><span>|</span><span>Sitemap</span><span>|</span><span>Privacy Policy</span><span>|</span><span>Advertise</span><span>|</span><span>Terms &amp; Use</span>
  </nav>
  <p class="copyright">© 2013, All Rights Reserved</p>
</footer>
</body>
</html>
```